Business Card for Bloom Vitality & Strength

Hi can you please design a business card with my logo and program logo (the new one I just sent) somewhere on it too maybe on the back? Needs to be eye catching and super cool.
Trudy Melcombe, Director
Master Personal Trainer & Nutrition Coach
0472 816 305
Www.bloomvitalitystrength.com.au
Insta (logo) bloom_vitality_strength #bloomyou7x72018

Target Market(s)

30+ women looking to change lifestyle to healthy mind body etc

Industry/Entity Type

Health And Wellness

Contact Information for Business Card

As above

Font styles to use
Sans Serif

Colors

Designer to choose colors to be used in the design.

Requirements
Must have
• Must super cool and edgy with a bit of cuteness

```html
<!DOCTYPE html>
<html lang="en">
<head>
<meta charset="utf-8">
<title>Bloom Vitality &amp; Strength – Business Card</title>
<link rel="stylesheet" href="https://fonts.googleapis.com/css2?family=Source+Sans+3:wght@400;600;700&display=swap">
<style>
  :root {
    --page: #ecebe8;
    --green: #00a55e;
    --red: #d41518;
    --red-dark: #c4141b;
    --white: #ffffff;
    --paper-top: #ffffff;
    --paper-bottom: #e6e6e6;
    --ink: #2b2b2b;
    --leaf: #cfe9d9;
  }
  * { box-sizing: border-box; margin: 0; padding: 0; }
  html, body { width: 1200px; height: 960px; overflow: hidden; }
  body {
    background: var(--page);
    position: relative;
    font-family: "Source Sans 3", sans-serif;
  }
  .card {
    position: absolute;
    width: 600px;
    height: 344px;
    border-radius: 22px;
    overflow: hidden;
    box-shadow: 0 3px 8px rgba(0,0,0,0.25);
  }
  .card-front { left: 302px; top: 118px; background: var(--green); }
  .card-back  { left: 298px; top: 498px; background: var(--red); }

  .front-shape { position: absolute; inset: 0; }

  .leaf-accent {
    position: absolute;
    left: 264px; top: 6px;
    width: 78px; height: 44px;
    border-radius: 50%;
    background: var(--leaf);
  }

  .contact-block {
    position: absolute;
    left: 34px; top: 104px;
    color: var(--white);
  }
  .person-name { font-size: 18px; font-weight: 700; line-height: 22px; }
  .person-role { font-size: 14.5px; font-weight: 600; line-height: 17px; }
  .contact-list { list-style: none; margin-top: 9px; }
  .contact-list li {
    display: flex; align-items: center; gap: 8px;
    font-size: 14px; line-height: 19px;
  }
  .contact-icon { width: 14px; height: 14px; flex: none; }

  .program-mark {
    position: absolute;
    left: 318px; top: 160px;
    width: 232px; height: 44px;
    display: flex; align-items: center; justify-content: center; gap: 10px;
  }
  .program-dot { width: 16px; height: 16px; border-radius: 50%; background: var(--red); flex: none; }
  .program-name {
    font-weight: 600;
    font-size: 26px;
    color: var(--ink);
  }

  .brand-mark {
    position: absolute;
    left: 0; right: 0; top: 118px;
    display: flex; align-items: center; justify-content: center; gap: 12px;
  }
  .brand-dot { width: 22px; height: 22px; border-radius: 50%; background: var(--white); }
  .brand-name { font-size: 30px; font-weight: 700; color: var(--white); }
  .back-url {
    position: absolute;
    left: 0; right: 0; top: 284px;
    text-align: center;
    color: var(--white);
    font-size: 13.5px;
    letter-spacing: 1.2px;
  }
  .back-url strong { font-weight: 700; }
</style>
</head>
<body>
  <section class="card card-front" aria-label="Business card front">
    <svg class="front-shape" viewBox="0 0 600 344" width="600" height="344" aria-hidden="true">
      <defs>
        <linearGradient id="paperFade" x1="0" y1="0" x2="0" y2="1">
          <stop offset="0" stop-color="#ffffff"/>
          <stop offset="1" stop-color="#e6e6e6"/>
        </linearGradient>
      </defs>
      <path d="M 333 0 C 258 70 244 210 338 344 L 600 344 L 600 0 Z" fill="#ffffff"/>
      <path d="M 337 0 C 263 72 250 210 344 344 L 600 344 L 600 0 Z" fill="#c4141b"/>
      <path d="M 345 0 C 278 60 262 200 356 344 L 600 344 L 600 0 Z" fill="url(#paperFade)"/>
    </svg>
    <div class="leaf-accent" role="img" aria-label="Two small green leaves"></div>

    <div class="contact-block">
      <p class="person-name">Trudy Melcombe</p>
      <p class="person-role">Director</p>
      <p class="person-role">Master Personal Trainer &amp;</p>
      <p class="person-role">Nutrition Coach</p>
      <ul class="contact-list">
        <li>
          <svg class="contact-icon" viewBox="0 0 16 16" aria-hidden="true"><path fill="#fff" d="M3.6 1.2 6 3.8 4.8 5.6c.9 2.2 3.4 4.7 5.6 5.6l1.8-1.2 2.6 2.4-1.6 2.2C7.8 14.4 1.6 8.2 1.4 2.8z"/></svg>
          0472 816 305
        </li>
        <li>
          <svg class="contact-icon" viewBox="0 0 16 16" aria-hidden="true"><circle cx="8" cy="8" r="6.5" fill="none" stroke="#fff" stroke-width="1.8"/><path d="M1.5 8h13M8 1.5c-3 3.5-3 9.5 0 13M8 1.5c3 3.5 3 9.5 0 13" fill="none" stroke="#fff" stroke-width="1.2"/></svg>
          bloomvitalitystrength.com.au
        </li>
        <li>
          <svg class="contact-icon" viewBox="0 0 16 16" aria-hidden="true"><rect x="1.5" y="1.5" width="13" height="13" rx="2" fill="#fff"/></svg>
          bloom_vitality_strength
        </li>
        <li>
          <svg class="contact-icon" viewBox="0 0 16 16" aria-hidden="true"><circle cx="8" cy="8" r="6.5" fill="#fff"/></svg>
          #bloomyou7x72018
        </li>
      </ul>
    </div>

    <div class="program-mark">
      <span class="program-dot"></span>
      <span class="program-name">BloomYou7x7</span>
    </div>
  </section>

  <section class="card card-back" aria-label="Business card back">
    <div class="brand-mark">
      <span class="brand-dot"></span>
      <span class="brand-name">Bloom Vitality &amp; Strength</span>
    </div>
    <p class="back-url">www.<strong>bloomvitalitystrength</strong>.com.au</p>
  </section>
</body>
</html>
```